Business Card Design

It's an investment advisory service for individuals with all there investment needs. Also financial consulting to businesses and governmental agencies on retirement plans etc. It's personalized not commoditized help. Should show strength, knowledge and money orientation.
Updates

Reason: Will be out of town setting up office.

Reason: waiting for the 2/3rds of group to vote

Reason: only half the votes are in, I'm calling and getting verbals, but at this time we are down to 2 designs.

Industry/Entity Type

Investment

Contact Information for Business Card

B. Rel K. Financial Consulting and Wealth Management, Desmond Wick Harlow, 5172 Paseo Loma Verde Crest, San Diego, CA 92131-4817, Registered Investment Advisor

Requirements
Nice to have
• Something money oriented

```html
<!DOCTYPE html>
<html lang="en">
<head>
<meta charset="utf-8">
<title>B. Rel K. Financial Consulting and Wealth Management — Business Card</title>
<link rel="stylesheet" href="https://fonts.googleapis.com/css2?family=Cantarell:wght@400;700&display=swap">
<style>
  :root {
    --navy: #080d2a;
    --mist: #c3c8cf;
    --paper: #ffffff;
    --ink: #111111;
    --seam: #9a9ea4;
  }
  html, body {
    margin: 0;
    padding: 0;
    width: 1200px;
    height: 702px;
    overflow: hidden;
    background: var(--paper);
  }
  .card {
    position: relative;
    width: 1200px;
    height: 702px;
    background: var(--paper);
    font-family: "Cantarell", "Helvetica Neue", Arial, sans-serif;
  }
  .brand-panel {
    position: absolute;
    left: 0;
    top: 0;
    width: 565px;
    height: 702px;
    background: var(--navy);
    box-shadow: 3px 0 2px var(--seam);
    color: var(--mist);
    text-align: center;
  }
  .brand-name {
    position: absolute;
    left: 0;
    width: 100%;
    top: 268px;
    margin: 0;
    font-size: 45px;
    font-weight: 400;
    line-height: 56px;
    letter-spacing: 0.5px;
  }
  .contact {
    position: absolute;
    left: 620px;
    top: 0;
    color: var(--ink);
  }
  .person-name {
    position: absolute;
    top: 258px;
    margin: 0;
    font-size: 39px;
    font-weight: 700;
    line-height: 1;
    white-space: nowrap;
  }
  .person-role {
    position: absolute;
    top: 304px;
    margin: 0;
    font-size: 36px;
    font-weight: 400;
    line-height: 1;
    white-space: nowrap;
    letter-spacing: 0.3px;
  }
  .address {
    position: absolute;
    top: 358px;
    margin: 0;
    font-style: normal;
    font-size: 21px;
    line-height: 28px;
    white-space: nowrap;
  }
</style>
</head>
<body>
  <main class="card">
    <section class="brand-panel">
      <h1 class="brand-name">B. Rel K. Financial<br>Consulting and<br>Wealth Management</h1>
    </section>
    <section class="contact">
      <h2 class="person-name">Desmond Wick Harlow</h2>
      <p class="person-role">Registered Investment Advisor</p>
      <address class="address">
        5172<br>
        Paseo Loma Verde Crest,<br>
        San Diego<br>
        CA 92131-4817
      </address>
    </section>
  </main>
</body>
</html>
```